Vocational Mentor needs an impressive business card

1. I need a business card (or maybe three with identic look) to promote me and my three business titles/services:
- Vocational Mentor. I help people find their vocation and live happily from it. I use my 20 years of experience in business, management and psychology to help them identify the most efficient ways to make a living doing what they are passionate about.
- Business Angel. I help founders start a succesful business with minimum risks and costs. I use my 20 years of experience in sales, management and entrepreneurship to help them identify the most efficient ways, in terms of time and cost, to validate their business idea.
- Learning Designer. I design unique learning programs that produce long-term cognitive and behavioural changes to people and organisations. I use my 20 years of experience in learning, teaching and change management to create minimalist experiences and processes that allow them to change efficiently in their pursued direction.

2. I would like a two-sided business card, on the front with my name, contact details and titles, on the back the explanation of the services.
Updates

Hi all,

I updated my brief, included contacts info and give feedback on all designs I got. I am new on this platform so please tell me if you need anything else or if I don't use corectly the platform forms.

Kind regards,
Tudor

Hi all,

I shortened the services description by deleting the phrase "I call..."

Kind regards,
Tudor

Target Market(s)

Freelancers, startups, people and organization willing to invest in change through ultimate learning experiences

Industry/Entity Type

Business

Font styles to use
Serif

Requirements
Must have
• Front side: full name, titles, web site, email, phone like below:
Tudor Vasilache
Vocational Mentor, Business Angel, Learning Designer
info@tudorvasilache.example
www.tudorvasilache.example
+40-745-TUDORV
Nice to have
• Back side: the description of the services I provide as in the task description.
1/3: it would be nice if I can jam all three titles on the front side but then I need a solution to jam all three services on the back side.

```html
<!DOCTYPE html>
<html lang="en">
<head>
<meta charset="UTF-8">
<title>Tudor Vasilache – Business Card</title>
<link rel="stylesheet" href="https://fonts.googleapis.com/css2?family=Lato:ital,wght@0,300;0,400;0,700;0,900;1,400&display=swap">
<style>
  :root {
    --brand-blue: #1f6fb5;
    --paper: #ffffff;
    --ink: #1a1a1a;
    --stage: #e9ebee;
    --on-blue: #ffffff;
  }
  * { margin: 0; padding: 0; box-sizing: border-box; }
  html, body {
    width: 1200px;
    height: 926px;
    overflow: hidden;
    background: var(--stage);
    font-family: "Lato", Arial, sans-serif;
  }
  .sheet {
    position: relative;
    width: 1200px;
    height: 926px;
  }
  .card {
    position: absolute;
    left: 260px;
    width: 680px;
    height: 412px;
    overflow: hidden;
    box-shadow: 0 6px 20px rgba(0,0,0,0.18);
  }
  .card--front { top: 36px; background: var(--paper); }
  .card--back  { top: 480px; background: var(--brand-blue); }

  .card__shape { position: absolute; inset: 0; }
  .card__shape path { fill: var(--brand-blue); }

  .identity {
    position: absolute;
    left: 24px;
    top: 34px;
  }
  .identity__name {
    font-weight: 700;
    font-size: 35px;
    letter-spacing: 0.5px;
    color: var(--brand-blue);
    line-height: 1;
  }
  .identity__titles {
    margin-top: 4px;
    font-style: italic;
    font-size: 13px;
    color: var(--ink);
    white-space: nowrap;
  }

  .contact {
    position: absolute;
    left: 322px;
    top: 288px;
    list-style: none;
    color: var(--on-blue);
    font-size: 19px;
    letter-spacing: 0.6px;
    line-height: 29px;
  }
  .contact__label { font-weight: 700; margin-right: 4px; }

  .services {
    position: absolute;
    left: 30px;
    top: 24px;
    right: 30px;
    color: var(--on-blue);
  }
  .service + .service { margin-top: 12px; }
  .service__title {
    font-weight: 300;
    font-size: 23px;
    text-transform: uppercase;
    letter-spacing: 0.3px;
    line-height: 1.15;
  }
  .service__title strong { font-weight: 900; }
  .service__text {
    font-size: 14.5px;
    line-height: 1.3;
    margin-top: 3px;
  }
</style>
</head>
<body>
<main class="sheet">

  <section class="card card--front" aria-label="Business card front">
    <svg class="card__shape" viewBox="0 0 680 412" width="680" height="412" aria-hidden="true">
      <path d="M300 0 H680 V412 H300 V284 L260 276 C284 268 300 250 300 222 Z"/>
    </svg>
    <div class="identity">
      <h1 class="identity__name">Tudor Vasilache</h1>
      <p class="identity__titles">Vocational Mentor, Business Angel, Learning Designer</p>
    </div>
    <ul class="contact">
      <li><span class="contact__label">P:</span>0400 555 019</li>
      <li><span class="contact__label">E:</span>info@tudorvasilache.example</li>
      <li><span class="contact__label">w:</span>www.tudorvasilache.example</li>
    </ul>
  </section>

  <section class="card card--back" aria-label="Business card back">
    <div class="services">
      <article class="service">
        <h2 class="service__title">Vocational <strong>Mentor</strong></h2>
        <p class="service__text">I help people to find their vocation and live happily from it. I use my 20 years of experience in business, management and psychology to help them identify the most efficient ways to make a living doing what they are passionate about.</p>
      </article>
      <article class="service">
        <h2 class="service__title">Business <strong>Angel</strong></h2>
        <p class="service__text">I help founders to start a succesful business with minimum risks and costs. I use my 20 years of experience in sales, management and entrepreneurship to help them identify the most efficient ways, in terms of time and cost, to validate their business idea.</p>
      </article>
      <article class="service">
        <h2 class="service__title">Learning <strong>Designer</strong></h2>
        <p class="service__text">I design unique learning programs that produce long-term cognitive and behavioural changes to people and organisations. I use my 20 years of experience in learning, teaching and change management to create minimalist experiences and processes that allows them to change efficiently in their pursued direction.</p>
      </article>
    </div>
  </section>

</main>
</body>
</html>
```